Cover Art Needed For Digital Single Release

We are looking to have the cover art designed for a new song called "Paper Lanterns". You will find the track attached below in a private Tunepool link so that you can have a listen.
We are thinking of keeping the artwork fairly simple but still want it to catch your eye. Maybe using the song title and artist’s name in a colorful and creative way. (A well-designed font with a bold color scheme, or even something like a mosaic style art piece featuring the title).
We completely welcome any and all creative visions you might have, even if it strays away from the examples given above.
Thank you in advance for your submissions, and we are excited to collaborate with you!
"Paper Lanterns" by Marcus Fell
https://tunepool.example/marcuszxq/paper-lanterns/s-r7tWnexiLqa
Target Market(s)
Teens/Young Adults
Industry/Entity Type
Music
Requirements
Must have
- An eye-catching design
Should not have
- Please do not rely heavily on stock images. We prefer an original design/concept.

```html
<!DOCTYPE html>
<html lang="en">
<head>
<meta charset="utf-8">
<title>Paper Lanterns — Cover and Disc Label</title>
<link href="https://fonts.googleapis.com/css2?family=Poiret+One&family=Montserrat:wght@500&display=swap" rel="stylesheet">
<style>
  :root {
    --page: #ffffff;
    --blue-deep: #3a8bff;
    --blue-soft: #8fbbff;
    --blue-pale: #b7d3ff;
    --ink: #0b5aa8;
    --ink-byline: #0b4f96;
  }
  html, body {
    margin: 0;
    padding: 0;
    width: 1200px;
    height: 1200px;
    overflow: hidden;
    background: var(--page);
  }
  .canvas {
    position: relative;
    width: 1200px;
    height: 1200px;
  }
  .cover {
    position: absolute;
    left: 99px;
    top: 172px;
    width: 487px;
    height: 487px;
  }
  .disc-label {
    position: absolute;
    left: 631px;
    top: 174px;
    width: 484px;
    height: 484px;
  }
  .title {
    font-family: "Poiret One", sans-serif;
    fill: var(--ink);
    letter-spacing: 1px;
  }
  .byline {
    font-family: "Montserrat", sans-serif;
    font-weight: 500;
    fill: var(--ink-byline);
  }
</style>
</head>
<body>
<main class="canvas">

  <svg class="cover" viewBox="0 0 487 487" aria-label="Paper Lanterns by Marcus Fell — single cover">
    <defs>
      <radialGradient id="backdropGlow" cx="0.5" cy="0.5" r="0.75">
        <stop offset="0" stop-color="var(--blue-pale)"/>
        <stop offset="0.55" stop-color="var(--blue-pale)"/>
        <stop offset="0.8" stop-color="var(--blue-soft)"/>
        <stop offset="1" stop-color="var(--blue-deep)"/>
      </radialGradient>
    </defs>
    <rect class="backdrop" width="487" height="487" fill="url(#backdropGlow)" role="img" aria-label="Abstract blue background artwork"/>
    <g class="title-block">
      <text class="title" x="104" y="248" font-size="88">PAPER</text>
      <text class="title" x="106" y="306" font-size="54">LANTERNS</text>
      <text class="byline" x="108" y="336" font-size="15">by Marcus Fell</text>
    </g>
  </svg>

  <svg class="disc-label" viewBox="0 0 484 484" aria-label="Paper Lanterns by Marcus Fell — disc label">
    <circle class="backdrop" cx="242" cy="242" r="242" fill="url(#backdropGlow)" role="img" aria-label="Abstract blue background artwork"/>
    <g class="title-block">
      <text class="title" x="180" y="110" font-size="74">PAPER</text>
      <text class="title" x="182" y="159" font-size="45">LANTERNS</text>
      <text class="byline" x="184" y="184" font-size="13">by Marcus Fell</text>
    </g>
  </svg>

</main>
</body>
</html>
```